Design and Renovation Company Luxury Business Card

I want to create a luxury business card for a Design and Renovation Firm . We will use our current logo. The company name is 742BUILD. We do not want anything standard. We need a very unique concept.
Please see uploaded inspiration. I really like the textured paper option. I would like the card to be thick with debossing, and/or embossing options. The logo has orange in it but I would like to see the card with and without the orange. I think the orange may make the company feel less high-end. The goal is to elevate the logo not match its vibe per se of the logo. We want something very unique, not standard at all!
I would like a space for :
Logo,
Name,
Position,
Email,
Office number,
Website Address,
Business Address,
Thank you!
Have fun!
Target Market(s)
Home owners Age 35 +
Industry/Entity Type
Design and Renovation
Contact Information for Business Card
Logo, Name, Position, Email, Office number, Website Address, Business Address,.
Colors
Designer to choose colors to be used in the design.
Requirements
Must have
- A luxury designer feel. Must be black or dark grey but open to other luxury ideas.
Nice to have
- Gold, silver, black embossing or debossing. Textured paper design.
Should not have
- A cheap look and feel.

```html
<!DOCTYPE html>
<html lang="en">
<head>
<meta charset="utf-8">
<title>742BUILD Business Card</title>
<link href="https://fonts.googleapis.com/css2?family=Montserrat:wght@400;500;700&display=swap" rel="stylesheet">
<style>
  :root {
    --backdrop: #2b2b2b;
    --card-black: #111111;
    --card-white: #ffffff;
    --ink: #111111;
    --accent: #f7941d;
    --rule: #222222;
    --white-text: #ffffff;
  }
  * { box-sizing: border-box; margin: 0; padding: 0; }
  html, body {
    width: 1200px; height: 1186px; overflow: hidden;
    background: var(--backdrop);
  }
  .canvas { position: relative; width: 1200px; height: 1186px; }
  .card {
    position: absolute; left: 150px; width: 900px; height: 514px;
    border-radius: 30px; overflow: hidden;
  }
  .card-back { top: 40px; background: var(--card-black); }
  .card-front { top: 606px; background: var(--card-white); }

  .brand-name {
    position: absolute;
    font-family: "Montserrat", sans-serif; font-weight: 700;
    font-size: 64px; line-height: 1;
  }
  .card-back .brand-name {
    left: 0; right: 0; top: 225px; text-align: center; color: var(--white-text);
  }
  .card-front .brand-name {
    left: 300px; top: 100px; color: var(--ink);
  }

  .divider {
    position: absolute; left: 150px; right: 60px; top: 222px;
    height: 1.5px; background: var(--rule);
  }
  .person { position: absolute; left: 60px; top: 262px; font-family: "Montserrat", sans-serif; color: var(--ink); }
  .person-name { font-weight: 700; font-size: 30px; }
  .person-role { font-weight: 400; font-size: 19px; margin-top: 2px; padding-bottom: 12px; border-bottom: 1.5px solid var(--rule); width: 230px; }
  .contact-list { list-style: none; margin-top: 14px; }
  .contact-list li { display: flex; align-items: center; gap: 12px; font-size: 19px; margin-bottom: 8px; }
  .contact-list svg { width: 18px; height: 18px; fill: var(--accent); flex: none; }

  .address {
    position: absolute; right: 40px; top: 318px; text-align: right;
    font-family: "Montserrat", sans-serif; font-weight: 500; font-style: normal; font-size: 18px;
    line-height: 1.3; color: var(--ink);
  }
  .band-black { position: absolute; left: 0; bottom: 0; width: 690px; height: 16px; background: var(--ink); }
  .band-accent { position: absolute; left: 696px; right: 0; bottom: 0; height: 36px; background: var(--accent); }
</style>
</head>
<body>
<main class="canvas">
  <section class="card card-back" aria-label="Card back">
    <div class="brand-name">742BUILD</div>
  </section>

  <section class="card card-front" aria-label="Card front">
    <div class="brand-name">742BUILD</div>
    <div class="divider"></div>

    <div class="person">
      <div class="person-name">Daniel Harper</div>
      <div class="person-role">Managing Director</div>
      <ul class="contact-list">
        <li>
          <svg viewBox="0 0 24 24" aria-hidden="true"><path d="M6.6 10.8a15 15 0 0 0 6.6 6.6l2.2-2.2a1 1 0 0 1 1-.25 11.4 11.4 0 0 0 3.6.57 1 1 0 0 1 1 1V20a1 1 0 0 1-1 1A17 17 0 0 1 3 4a1 1 0 0 1 1-1h3.5a1 1 0 0 1 1 1c0 1.250.2 2.45.57 3.57a1 1 0 0 1-.25 1z"/></svg>
          555-014-2290
        </li>
        <li>
          <svg viewBox="0 0 24 24" aria-hidden="true"><path d="M2 5h20v14H2z M2 5l10 8 10-8" stroke="#fff" stroke-width="1.5"/></svg>
          hello@742build-studio.com
        </li>
        <li>
          <svg viewBox="0 0 24 24" aria-hidden="true"><circle cx="12" cy="12" r="10"/><path d="M2 12h20M12 2c3 3 3 17 0 20M12 2c-3 3-3 17 0 20" stroke="#fff" stroke-width="1.3" fill="none"/></svg>
          www.742build-studio.com
        </li>
      </ul>
    </div>

    <address class="address">418 Maple Grove Ave, #112<br>Fairview, OH 43210</address>

    <div class="band-black"></div>
    <div class="band-accent"></div>
  </section>
</main>
</body>
</html>
```